Meridale Clinical Spa needs an eye-catching poster to help promote our largest sale of spring!

We need a poster that will go on the back of the doors in the patient rooms. Our medical spa is professional and high-end, so we want the poster to look sophisticated, yet very eye-catching.
This project is for our Sunny Soiree special, our second largest sale of the year.

Name: Sunny Soiree
Slogan: Let Your Beauty Bloom
Sale: The More You Buy, The More You Save

Choose from your favorite spa services
VELUNA, Laser Treatments, Microderms, and More!

It would be great to have something blooming. Flowers, or somehow make a woman look like she's blooming.

I am attaching a visual description of our special. However, the poster should NOT include the pricing tiers. I am also attaching our business logo. Thank you!!

Target Market(s)

A majority are women, but some are men. Around 25-55 in age. Middle to upper class who are likely to spend more money.

Industry/Entity Type

Medical

Font styles to use
Sans Serif
Script

Colors

Designer to choose colors to be used in the design.

Requirements
Must have
• Name of promotion: Sunny Soiree
• Slogan: "Let Your Beauty Bloom"
• Concept "The more you buy, the more you save on your favorite spa services"
• Select from your favorite spa services such as VELUNA, laser treatments, microderms, and more!
• Website: MeridaleSpaSpecials.com
• Our logo (attached)
Nice to have
• Modern and creative design. Somehow tying in the "Let your beauty bloom" theme. We don't want the focus to be "The more you buy the more you save"
• We are looking for a unique design that is unlike traditional medical spas in the area that typically include a lot of white and a lot of overly photoshopped images.
• Creativity is key! Something that's different than just text and images. We would be so excited to see that!
Should not have
• Not too much text, but enough to get the point across.

```html
<!DOCTYPE html>
<html lang="en">
<head>
<meta charset="utf-8">
<title>Sunny Soiree – Meridale Clinical Spa</title>
<link rel="stylesheet" href="https://fonts.googleapis.com/css2?family=Libre+Baskerville:ital,wght@0,400;0,700;1,400&family=Playfair+Display:wght@800&family=Kaushan+Script&display=swap">
<style>
  :root {
    --canvas: #efe9e4;
    --frame: #ffffff;
    --pink-deep: #e0197a;
    --pink-bloom: #c94f96;
    --pink-mid: #e98fc0;
    --pink-soft: #f4cde3;
    --pink-pale: #fbeaf3;
    --plum: #7d1650;
    --script-blue: #2f6fb2;
    --badge-blue: #2d6aa8;
    --date-black: #111111;
    --band-pink: #d92a7c;
    --logo-panel: #f5f1ef;
    --logo-ink: #2b2b2b;
    --white: #ffffff;
  }
  * { box-sizing: border-box; margin: 0; padding: 0; }
  html, body {
    width: 1200px; height: 864px; overflow: hidden;
    background: var(--canvas);
  }
  .poster {
    position: absolute; left: 330px; top: 22px;
    width: 540px; height: 820px;
    background: var(--frame);
    padding: 18px;
    box-shadow: 0 2px 10px rgba(0,0,0,.12);
  }
  .poster-art {
    position: relative; width: 100%; height: 100%; overflow: hidden;
  }
  .hero-photo {
    position: absolute; inset: 0;
    background:
      radial-gradient(ellipse 38% 26% at 86% 10%, var(--pink-bloom) 0, rgba(201,79,150,.55) 45%, rgba(201,79,150,0) 100%),
      radial-gradient(ellipse 24% 18% at 62% 4%, var(--pink-mid) 0, rgba(233,143,192,0) 100%),
      radial-gradient(ellipse 30% 40% at 94% 40%, #d98bbb 0, rgba(217,139,187,0) 100%),
      radial-gradient(ellipse 42% 34% at 64% 34%, var(--pink-pale) 0, rgba(251,234,243,0) 100%),
      radial-gradient(circle at 18% 88%, #c97aaa 0, rgba(201,122,170,0) 32%),
      linear-gradient(165deg, #f2c3dc 0%, #ecb4d3 50%, #de9cc4 100%);
  }
  .brand-panel {
    position: absolute; left: 29px; top: 1px;
    width: 278px; height: 119px;
    background: var(--logo-panel);
    border-radius: 0 0 6px 6px;
    display: flex; align-items: center; justify-content: center; gap: 12px;
  }
  .brand-dot {
    width: 16px; height: 16px; border-radius: 50%;
    background: var(--pink-deep);
  }
  .brand-name {
    font-family: "Libre Baskerville", serif;
    font-weight: 400; font-size: 21px;
    color: var(--logo-ink);
  }
  .services {
    position: absolute; left: 30px; top: 168px;
    width: 250px;
    font-family: "Libre Baskerville", serif;
    font-size: 17px; line-height: 1.45;
    color: var(--plum);
  }
  .services-lead {
    display: block; font-style: italic; font-size: 15px; margin-bottom: 4px;
  }
  .services strong { font-weight: 700; }
  .promo-title {
    position: absolute; left: 14px; top: 290px;
    font-family: "Playfair Display", serif;
    font-weight: 800; font-size: 90px; line-height: .86;
    color: var(--pink-deep);
    letter-spacing: -1px;
    text-shadow: 2px 2px 0 rgba(255,255,255,.6);
  }
  .slogan {
    position: absolute; left: 30px; top: 478px;
    font-family: "Kaushan Script", cursive;
    font-size: 46px;
    color: var(--script-blue);
    transform: rotate(-7deg);
    transform-origin: left center;
    white-space: nowrap;
  }
  .sale-dates {
    position: absolute; left: 0; top: 588px;
    width: 330px; height: 56px;
    background: linear-gradient(90deg, var(--date-black) 55%, rgba(17,17,17,.55) 100%);
    color: var(--white);
    font-family: "Libre Baskerville", serif;
    font-weight: 700; font-size: 26px;
    display: flex; align-items: center; padding-left: 30px;
  }
  .savings-badge {
    position: absolute; left: 318px; top: 530px;
    width: 180px; height: 180px;
  }
  .savings-badge svg { position: absolute; inset: 0; width: 100%; height: 100%; }
  .savings-text {
    position: absolute; inset: 0;
    display: flex; flex-direction: column; align-items: center; justify-content: center;
    transform: rotate(-20deg);
    font-family: "Libre Baskerville", serif;
    font-size: 17px; line-height: 1.02;
    color: var(--white); text-align: center;
  }
  .savings-text strong { font-weight: 700; font-size: 20px; }
  .web-band {
    position: absolute; left: 0; right: 0; bottom: 0;
    height: 46px;
    background: var(--band-pink);
    color: var(--white);
    font-family: "Libre Baskerville", serif;
    font-size: 19px; letter-spacing: 1px;
    display: flex; align-items: center; padding-left: 16px;
  }
</style>
</head>
<body>
  <main class="poster">
    <div class="poster-art">
      <div class="hero-photo" role="img" aria-label="Soft pink photograph of a smiling woman with blooming pink flowers in her hair"></div>

      <div class="brand-panel">
        <span class="brand-dot"></span>
        <span class="brand-name">Meridale Clinical Spa</span>
      </div>

      <p class="services">
        <span class="services-lead">Choose from your favorite spa services</span>
        <strong>VELUNA</strong>, Laser Treatments, Microderms &amp; More!
      </p>

      <h1 class="promo-title">SUNNY<br>SOIREE</h1>
      <p class="slogan">let your beauty bloom</p>

      <p class="sale-dates">April 20 - June 2</p>

      <div class="savings-badge">
        <svg viewBox="-100 -100 200 200" aria-hidden="true">
          <polygon fill="var(--badge-blue)" points="96,0 83,13.1 91.3,29.7 74.8,38.1 77.7,56.4 59.4,59.4 56.4,77.7 38.1,74.8 29.7,91.3 13.1,83 0,96 -13.1,83 -29.7,91.3 -38.1,74.8 -56.4,77.7 -59.4,59.4 -77.7,56.4 -74.8,38.1 -91.3,29.7 -83,13.1 -96,0 -83,-13.1 -91.3,-29.7 -74.8,-38.1 -77.7,-56.4 -59.4,-59.4 -56.4,-77.7 -38.1,-74.8 -29.7,-91.3 -13.1,-83 0,-96 13.1,-83 29.7,-91.3 38.1,-74.8 56.4,-77.7 59.4,-59.4 77.7,-56.4 74.8,-38.1 91.3,-29.7 83,-13.1"/>
        </svg>
        <p class="savings-text">
          <span>THE MORE</span>
          <span>YOU <strong>BUY</strong></span>
          <span>THE MORE</span>
          <span>YOU <strong>SAVE</strong></span>
        </p>
      </div>

      <p class="web-band">MeridaleSpaSpecials.com</p>
    </div>
  </main>
</body>
</html>
```